Letterhead for new real estate company in South Africa named Lofthaven

A letterhead with the directors and company details to be editable as these changes often

Target Market(s)

In line with our logo brief and our newly designed logo and corporate fee

Industry/Entity Type

Real Estate

Requirements
Must have
• Details as per the sample letterhead provided.

```html
<!DOCTYPE html>
<html lang="en">
<head>
<meta charset="utf-8">
<title>Lofthaven Letterhead</title>
<link rel="stylesheet" href="https://fonts.googleapis.com/css2?family=Open+Sans:wght@400;600;700&display=swap">
<style>
  :root {
    --paper: #fbfbfb;
    --ink: #5a5a5a;
    --ink-strong: #4a4a4a;
    --green: #36ad6c;
    --brown: #736352;
    --signature: #2b2a6e;
    --white: #ffffff;
  }
  * { box-sizing: border-box; margin: 0; padding: 0; }
  html, body { width: 1100px; height: 1200px; overflow: hidden; background: var(--paper); }
  body { font-family: "Open Sans", Arial, sans-serif; color: var(--ink); }

  .letterhead { position: relative; width: 1100px; height: 1200px; background: var(--paper); overflow: hidden; }

  .brand { position: absolute; left: 80px; top: 100px; display: flex; align-items: center; gap: 14px; }
  .brand-dot { width: 40px; height: 40px; border-radius: 50%; background: var(--green); }
  .brand-name { font-size: 46px; font-weight: 600; color: var(--green); letter-spacing: -0.5px; line-height: 1; }

  .salutation { position: absolute; left: 119px; top: 300px; font-size: 15px; }

  .letter-body { position: absolute; left: 84px; top: 364px; width: 932px; font-size: 15px; line-height: 22px; text-align: justify; }
  .letter-body p { text-indent: 35px; margin-bottom: 21px; }

  .sign-off { position: absolute; left: 119px; top: 862px; font-size: 14.5px; }
  .sign-off .signer { font-weight: 700; color: var(--ink-strong); }
  .signature { display: block; width: 210px; height: 44px; margin: 14px 0 12px -4px; border-radius: 6px; background: linear-gradient(90deg, rgba(43,42,110,0.16), rgba(43,42,110,0.06)); }

  .footer-wave { position: absolute; left: 0; top: 1028px; width: 1100px; height: 172px; }

  .contact { position: absolute; right: 64px; top: 1094px; text-align: right; color: var(--white); font-size: 16.5px; line-height: 21px; }
  .contact li { list-style: none; display: flex; justify-content: flex-end; align-items: center; gap: 8px; }
  .contact svg { width: 14px; height: 14px; fill: var(--white); }
  .contact .address { margin-top: 4px; padding-right: 0; }
</style>
</head>
<body>
<main class="letterhead">
  <header class="brand">
    <span class="brand-dot"></span>
    <span class="brand-name">LOFTHAVEN</span>
  </header>

  <p class="salutation">Dear Sir,</p>

  <section class="letter-body">
    <p>Lorem Ipsum is simply dummy text of the printing and typesetting industry. Lorem Ipsum has been the industry's standard dummy text ever since the 1500s, when an unknown printer took a galley of type and scrambled it to make a type specimen book. It has survived not only five centuries, but also the leap into electronic typesetting, remaining essentially unchanged. It was popularised in the 1960s with the release of Letraset sheets containing Lorem Ipsum passages, and more recently with desktop publishing software like Aldus PageMaker including versions of Lorem Ipsum.</p>
    <p>Lorem Ipsum is simply dummy text of the printing and typesetting industry. Lorem Ipsum has been the industry's standard dummy text ever since the 1500s, when an unknown printer took a galley of type and scrambled it to make a type specimen book. It has survived not only five centuries, but also the leap into electronic typesetting, remaining essentially unchanged. It was popularised in the 1960s with the release of Letraset sheets containing Lorem Ipsum passages, and more recently with desktop publishing software like Aldus PageMaker including versions of Lorem Ipsum.</p>
    <p>Lorem Ipsum is simply dummy text of the printing and typesetting industry. Lorem Ipsum has been the industry's standard dummy text ever since the 1500s, when an unknown printer took a galley of type and scrambled it to make a type specimen book. It was popularised in the 1960s with the release of Letraset sheets containing Lorem Ipsum passages, and more recently with desktop publishing software like Aldus PageMaker including versions of Lorem Ipsum.</p>
    <p>It was popularised in the 1960s with the release of Letraset sheets containing Lorem Ipsum passages, and more recently with desktop publishing software like Aldus PageMaker including versions of Lorem Ipsum.</p>
  </section>

  <section class="sign-off">
    <p class="signer">Your Name</p>
    <span class="signature" role="img" aria-label="Handwritten signature of Marcus Teller"></span>
    <p class="role">CEO &nbsp;|&nbsp; Owner</p>
  </section>

  <svg class="footer-wave" viewBox="0 0 1100 172" preserveAspectRatio="none" aria-hidden="true">
    <path fill="var(--green)" d="M0,112 C180,190 480,172 700,100 C860,48 980,24 1100,32 L1100,172 L0,172 Z"/>
    <path fill="var(--brown)" d="M0,42 C110,110 300,148 520,112 C720,78 900,-2 1100,4 L1100,20 C900,18 760,84 560,130 C330,182 110,150 0,84 Z"/>
    <path fill="var(--brown)" d="M70,92 C260,160 500,170 700,96 C540,160 300,170 70,92 Z"/>
  </svg>

  <ul class="contact">
    <li>0412557804
      <svg viewBox="0 0 16 16"><path d="M3 2h3l1.5 3.5-2 1.2a8 8 0 0 0 3.8 3.8l1.2-2L14 10v3a1 1 0 0 1-1 1A11 11 0 0 1 2 3a1 1 0 0 1 1-1z"/></svg>
    </li>
    <li>www.yourwebsite.com
      <svg viewBox="0 0 16 16"><path d="M8 1a7 7 0 1 0 0 14A7 7 0 0 0 8 1zm0 1.5c.9 0 1.8 1.9 2 4.5H6c.2-2.6 1.1-4.5 2-4.5zM2.6 7h2c.1-1.7.5-3.1 1-4A5.6 5.6 0 0 0 2.6 7zm0 2a5.6 5.6 0 0 0 3 4c-.5-.9-.9-2.3-1-4zm3.4 0h4c-.2 2.6-1.1 4.5-2 4.5S6.2 11.6 6 9zm5.4 0c-.1 1.7-.5 3.1-1 4a5.6 5.6 0 0 0 3-4zm0-2h2a5.6 5.6 0 0 0-3-4c.5.9.9 2.3 1 4z"/></svg>
    </li>
    <li>marcusteller@website.com
      <svg viewBox="0 0 16 16"><path d="M1 3h14v10H1zm1.5 1.5v.3L8 8.6l5.5-3.8v-.3zm0 2.1v4.9h11V6.6L8 10.4z"/></svg>
    </li>
    <li class="address">18 Wattle Crescent Seaford North VIC</li>
  </ul>
</main>
</body>
</html>
```